Vegan Jerky company needs a label for it's pouch, and a new logo

Dear Designers - this used to be a guaranteed project, however, due to the low quality of designs I have received, I have removed the guaranteed status. However, we need this product made and we will pay for a great, high quality design that meets the requirements of our brief.

We need sticker labels that will go onto the front and back of our vegan jerky package. Our package is a zip-sealable pouch, and we will either go with black, white or brown for the color of the pouch.

We need the concept, artwork, theme and logo designed. Pls choose the colors.

There will be four flavors. These can be finished as part of another project. The flavors are: Smoked Maple, Cracked Pepper, Teriyaki Sriracha, Original.

We are Lonny and Perla's Vegan Jerky.

Our food is vegan, non GMO, straight from the farm, organic, healthy, pure, clean, made in small batches and earth friendly. We use no chemicals or artificial flavors and our product is 100% natural.

Our kitchen is yours.

Target Market(s)

Vegetarians, vegans, health conscious, ecological, intelligent, caring.

Industry/Entity Type

Food Production

Logo Text

"Lonny and Perla" and "Our Kitchen is Yours"

Colors

Designer to choose colors to be used in the design.

Requirements
Must have
• earth friendly design, classy, hipster, vegan design, shabby chic,
Nice to have
• i have no ideas really...
• We prefer black and while, with a little splash of color. The last file is an idea I had but please use your own vision.

```html
<!DOCTYPE html>
<html lang="en">
<head>
<meta charset="utf-8">
<title>Lonny and Perla's Vegan Jerky – Pouch Label</title>
<link rel="stylesheet" href="https://fonts.googleapis.com/css2?family=Almendra&family=Smokum&family=Cormorant+Garamond:wght@500&display=swap">
<style>
  :root {
    --label-black: #050505;
    --label-charcoal: #1a1a1a;
    --gold: #d9a81f;
    --gold-light: #f0c94a;
    --gold-deep: #b8891a;
  }
  html, body {
    margin: 0;
    padding: 0;
    overflow: hidden;
  }
  .label {
    position: relative;
    width: 1200px;
    height: 1200px;
    background: radial-gradient(ellipse at 45% 35%, var(--label-charcoal) 0%, var(--label-black) 60%);
    overflow: hidden;
  }
  .label-frame,
  .label-type {
    position: absolute;
    inset: 0;
  }
  .brand-mark {
    position: absolute;
    left: 533px;
    top: 138px;
    width: 134px;
    height: 134px;
    box-sizing: border-box;
    border: 4px solid var(--gold);
    border-radius: 50%;
  }
  .brand-name {
    font-family: "Almendra", serif;
    font-weight: 400;
    font-size: 78px;
    fill: var(--gold);
  }
  .product-name {
    font-family: "Smokum", serif;
    font-weight: 400;
    font-size: 180px;
    fill: var(--gold);
  }
  .flourish {
    position: absolute;
    left: 395px;
    top: 470px;
    width: 410px;
    height: 64px;
    background: linear-gradient(90deg, transparent 0%, rgba(217,168,31,0.35) 20%, rgba(217,168,31,0.15) 50%, rgba(217,168,31,0.35) 80%, transparent 100%);
    border-radius: 32px;
  }
  .natural-seal {
    position: absolute;
    left: 494px;
    top: 898px;
    width: 212px;
    height: 114px;
  }
  .natural-seal-text {
    position: absolute;
    inset: 0;
    display: flex;
    flex-direction: column;
    align-items: center;
    justify-content: center;
    font-family: "Cormorant Garamond", serif;
    font-weight: 500;
    font-variant-numeric: lining-nums;
    color: var(--gold);
    line-height: 1;
  }
  .natural-seal-text .percent {
    font-size: 34px;
  }
  .natural-seal-text .percent sup {
    font-size: 14px;
  }
  .natural-seal-text .word {
    font-size: 24px;
    letter-spacing: 1px;
    margin-top: 2px;
  }
</style>
</head>
<body>
<main class="label">
  <svg class="label-frame" width="1200" height="1200" viewBox="0 0 1200 1200" aria-hidden="true">
    <defs>
      <linearGradient id="goldLine" x1="0" y1="0" x2="1" y2="1">
        <stop offset="0" stop-color="#f0c94a"/>
        <stop offset="0.5" stop-color="#d9a81f"/>
        <stop offset="1" stop-color="#b8891a"/>
      </linearGradient>
    </defs>
    <path d="M274,60 H926 A40,40 0 0 0 966,100 V1100 A40,40 0 0 0 926,1140 H274 A40,40 0 0 0 234,1100 V100 A40,40 0 0 0 274,60 Z"
          fill="none" stroke="url(#goldLine)" stroke-width="4"/>
  </svg>

  <div class="brand-mark" aria-hidden="true"></div>

  <div class="flourish" role="img" aria-label="Gold scrollwork flourish with small leaves beneath the brand name"></div>

  <svg class="label-type" width="1200" height="1200" viewBox="0 0 1200 1200">
    <text class="brand-name" x="600" y="442" text-anchor="middle" textLength="465" lengthAdjust="spacingAndGlyphs">Lonny &amp; Perla's</text>
    <text class="product-name" x="600" y="767" text-anchor="middle" textLength="540" lengthAdjust="spacingAndGlyphs">VEGAN JERKY</text>
  </svg>

  <div class="natural-seal">
    <svg width="212" height="114" viewBox="0 0 212 114" aria-hidden="true">
      <ellipse cx="106" cy="57" rx="102" ry="52" fill="none" stroke="var(--gold)" stroke-width="2.5"/>
      <ellipse cx="106" cy="57" rx="94" ry="46" fill="none" stroke="var(--gold-deep)" stroke-width="1.5"/>
    </svg>
    <div class="natural-seal-text">
      <span class="percent">100<sup>%</sup></span>
      <span class="word">NATURAL</span>
    </div>
  </div>
</main>
</body>
</html>
```